Fitness company needs new web design

We are looking to get our current site design improved to a newer design to better match our logo and features.

Current Site:
brinovamotion.com

* We would like the site to be modern/simple.
* The site will need to have the ability to take payments via stripe.
* We would like a "shop" page, as we will be selling supplements. Possible linkup with Shopify.
* The main landing page should flow in a way to sell our personal training & diet services. We would like the user to have to input their info (like we currently have) before placing an order.

We like how this site is put together: lumarifit.com

We use this service for our mobile app that our clients get to use when they signup: trelvacoach.net

If you have any questions please message use before starting your design.

Target Market(s)

Weight Loss, Fitness, Sports Athletes

Industry/Entity Type

Fitness

Coding

Coded - Design and coding required

Number of Pages Required

5+ page

Colors

Designer to choose colors to be used in the design.

Requirements
Must have
• Menu Tabs:
• - Programs
• - We offer 3 programs (see below for complete details)
• * Basic
• * Premium
• * Elite
• - Supplements
• - We currently have 2 supplements (see attached labels)
• * Vima Rise
• * Vima Blaze
• - About
• - FAQ
• - Contact
• - Book Appointment (calendly.com)
• Program Breakdown:
• Basic: Price $99/month
• - One 30 Minute In-Person or Phone Consultation
• - Unlimited in-app text support
• - Basic Nutrition Education
• - 30 Day Meal Plan
• Premium: Price $149/month
• - Two 30 Minute In-Person or Phone Consultations
• - Unlimited In-App Messaging Support
• - Customized Strength Training Program
• - Each Exercise Demonstrated in HD Videos
• - Personalized Cardio Program
• - Personalized Nutrition Coaching & Meal Plans
• Elite: Price $249/month
• - Weekly 30 Minute In-Person or Phone Consultation
• - Weekly Customized Strength Training Program
• - Weekly Customized Cardio Training Program
• - Bi-Weekly Nutrition Coaching & Meal Plans
Nice to have
• Click through form that collects clients information (like we have on our current site brinovamotion.com

```html
<!DOCTYPE html>
<html lang="en">
<head>
<meta charset="utf-8">
<title>Brinova Motion – Online Personal Training</title>
<link href="https://fonts.googleapis.com/css2?family=Lato:wght@400;700;900&display=swap" rel="stylesheet">
<style>
:root{
  --yellow:#f4ee1e;
  --ink:#222222;
  --dark:#3a3a3a;
  --darker:#2b2b2b;
  --black:#161616;
  --text:#333333;
  --muted:#555555;
  --light:#f1f1f1;
  --white:#ffffff;
}
*{box-sizing:border-box;margin:0;padding:0}
html,body{width:1200px;height:4534px;overflow:hidden}
body{position:relative;font-family:"Lato",Arial,sans-serif;color:var(--text);background:var(--white)}
.abs{position:absolute}
.btn{position:absolute;display:flex;align-items:center;justify-content:center;font-weight:700;font-size:15px;letter-spacing:.5px;text-transform:uppercase;height:52px}
.btn-dark{background:var(--darker);color:var(--white)}
.btn-yellow{background:var(--yellow);color:var(--ink)}
.section-mark{position:absolute;left:570px;width:60px;height:60px;border-radius:50%;border:6px solid var(--yellow)}
.section-title{position:absolute;left:0;width:1200px;text-align:center;font-weight:700;font-size:36px;text-transform:uppercase;color:var(--ink)}
.underline{position:absolute;left:560px;width:80px;height:5px;background:var(--yellow)}
.body-copy{font-size:15.5px;line-height:34px}

/* header */
.site-header{position:absolute;left:0;top:0;width:1200px;height:163px;background:var(--black)}
.brand{position:absolute;left:58px;top:62px;display:flex;align-items:center;gap:12px;color:var(--yellow);font-weight:700;font-size:17px;letter-spacing:1.5px;text-transform:uppercase}
.brand-dot{width:22px;height:22px;border-radius:50%;background:var(--yellow)}
.main-nav a{position:absolute;top:74px;color:var(--white);font-size:13px;font-weight:700;text-decoration:none;text-transform:uppercase}
.book{position:absolute;left:855px;top:0;width:270px;height:163px;background:var(--yellow);color:var(--ink);font-weight:900;font-size:19px;display:flex;align-items:center;justify-content:center;text-transform:uppercase}

/* hero */
.hero{position:absolute;left:0;top:163px;width:1200px;height:514px;background:linear-gradient(100deg,#6b6560 0%,#a39c94 40%,#d9d2c8 70%,#b8aea4 100%)}
.hero-title{position:absolute;left:75px;top:195px;color:var(--white);font-weight:900;font-size:44px;line-height:52px;text-transform:uppercase}
.dots{position:absolute;left:75px;top:452px;display:flex;gap:10px}
.dots span{width:11px;height:11px;border-radius:50%;background:rgba(255,255,255,.6)}
.dots span:first-child{background:var(--white)}

/* welcome */
.welcome-copy{position:absolute;left:100px;top:880px;width:1000px;text-align:center;color:var(--muted)}

/* programs */
.programs{position:absolute;left:0;top:1188px;width:1200px;height:871px;background:linear-gradient(130deg,#f6f3a0 0%,#f4ee1e 30%,#eeeeee 55%,#dcdcdc 75%,#e6df3a 100%)}
.plan{position:absolute;top:1427px;width:330px;height:553px;background:var(--white);overflow:hidden;box-shadow:0 4px 18px rgba(0,0,0,.15)}
.plan-corner{position:absolute;right:0;bottom:0;width:330px;height:553px}
.plan h3{position:absolute;top:36px;width:100%;text-align:center;font-size:24px;font-weight:700;text-transform:uppercase;color:var(--ink)}
.price{position:absolute;top:74px;left:50%;transform:translateX(-50%);background:var(--yellow);padding:4px 18px 6px;text-align:center;color:var(--ink)}
.price b{font-size:64px;font-weight:900;line-height:64px}
.price sup{font-size:28px;font-weight:900;vertical-align:30px}
.price small{display:block;font-size:15px;font-weight:700;margin-top:-4px}
.features{position:absolute;top:180px;left:30px;right:22px;list-style:none;font-size:15px;line-height:22px;color:var(--ink)}
.features li{position:relative;padding-left:30px;margin-bottom:1px}
.features li svg{position:absolute;left:0;top:5px}
.plan .btn{left:70px;bottom:38px;width:190px}

/* supplements */
.supplements{position:absolute;left:0;top:2059px;width:1200px;height:888px;background:var(--dark)}
.product-name{position:absolute;font-weight:900;font-size:37px;text-transform:uppercase}
.product-name span{color:var(--yellow)}
.prod-bar{position:absolute;width:60px;height:5px;background:var(--yellow)}
.product-image{position:absolute}

/* about */
.about{position:absolute;left:0;top:3591px;width:1200px;height:686px;background:var(--light)}

/* footer */
.site-footer{position:absolute;left:0;top:4277px;width:1200px;height:257px;background:var(--white)}
.subscribe-label{position:absolute;left:441px;top:4342px;font-weight:900;font-size:21px;color:var(--ink);text-transform:uppercase}
.subscribe-input{position:absolute;left:647px;top:4325px;width:353px;height:56px;border:1px solid #cccccc;background:var(--white);font-size:13px;color:#777777;padding-left:20px;display:flex;align-items:center}
.subscribe-btn{position:absolute;left:1000px;top:4325px;width:122px;height:56px;background:var(--yellow);font-weight:900;font-size:14px;display:flex;align-items:center;justify-content:center;color:var(--ink)}
.foot-nav a{position:absolute;top:4430px;font-size:13px;font-weight:700;color:var(--ink);text-decoration:none;text-transform:uppercase}
.social{position:absolute;top:4478px;width:20px;height:20px;border-radius:50%;background:var(--ink)}
</style>
</head>
<body>

<header class="site-header">
  <div class="brand"><span class="brand-dot"></span>Brinova Motion</div>
  <nav class="main-nav">
    <a style="left:285px" href="#">Home</a>
    <a style="left:366px" href="#">Programs</a>
    <a style="left:478px" href="#">About</a>
    <a style="left:566px" href="#">FAQ</a>
    <a style="left:630px" href="#">Contact</a>
    <a style="left:732px" href="#">Supplements</a>
  </nav>
  <a class="book">Book Appointment</a>
</header>

<section class="hero" role="img" aria-label="Photo of a woman doing a plank workout at home in front of a laptop">
  <h1 class="hero-title">Online Personal Training<br>and Diet Services</h1>
  <div class="dots"><span></span><span></span><span></span><span></span></div>
</section>

<section class="welcome">
  <div class="section-mark" style="top:710px"></div>
  <h2 class="section-title" style="top:783px">Welcome to Brinova Motion</h2>
  <div class="underline" style="top:838px"></div>
  <p class="welcome-copy body-copy">Lorem ipsum dolor sit amet, consectetur adipisicing elit, sed do eiusmod tempor incididunt ut labore et doloreades magna aliqua.<br>Ut enim ad minim veniam, quis nostrud exercitation ullamco laboris nisi ut aliquip ex ea commodo consequat. Duis aute irure dolor in<br>reprehenderit in voluptate velit esse cillum dolore eu fugiat nulla pariatur. Excepteur sint occaecat cupidatat non proident,<br>sunt in culpa qui officia deserunt mollit anim id est laborum.</p>
  <a class="btn btn-dark" style="left:511px;top:1058px;width:178px">Read More</a>
</section>

<section class="programs" role="img" aria-label="Yellow and grey geometric background"></section>
<div class="section-mark" style="top:1234px"></div>
<h2 class="section-title" style="top:1306px">Programs Plans</h2>
<div class="underline" style="top:1360px"></div>

<div class="plan" style="left:79px">
  <svg class="plan-corner" viewBox="0 0 330 553"><polygon points="330,120 330,553 120,553" fill="#f4ee1e" opacity=".35"/></svg>
  <h3>Basic</h3>
  <div class="price"><sup>$</sup><b>99</b><small>month</small></div>
  <ul class="features">
    <li><svg width="14" height="12"><path d="M1 6l4 4 8-9" stroke="#222" stroke-width="2.4" fill="none"/></svg>One 30 Minute In-Person or Phone Consultation</li>
    <li style="margin-top:13px"><svg width="14" height="12"><path d="M1 6l4 4 8-9" stroke="#222" stroke-width="2.4" fill="none"/></svg>Unlimited in-app text support</li>
    <li style="margin-top:13px"><svg width="14" height="12"><path d="M1 6l4 4 8-9" stroke="#222" stroke-width="2.4" fill="none"/></svg>Basic Nutrition Education</li>
    <li style="margin-top:13px"><svg width="14" height="12"><path d="M1 6l4 4 8-9" stroke="#222" stroke-width="2.4" fill="none"/></svg>30 Day Meal Plan</li>
  </ul>
  <a class="btn btn-dark">More Details</a>
</div>

<div class="plan" style="left:435px">
  <svg class="plan-corner" viewBox="0 0 330 553"><polygon points="330,120 330,553 120,553" fill="#f4ee1e" opacity=".35"/></svg>
  <h3>Premium</h3>
  <div class="price"><sup>$</sup><b>149</b><small>month</small></div>
  <ul class="features">
    <li><svg width="14" height="12"><path d="M1 6l4 4 8-9" stroke="#222" stroke-width="2.4" fill="none"/></svg>Two 30 Minute In-Person or Phone Consultations</li>
    <li><svg width="14" height="12"><path d="M1 6l4 4 8-9" stroke="#222" stroke-width="2.4" fill="none"/></svg>Unlimited In-App Messaging Support</li>
    <li><svg width="14" height="12"><path d="M1 6l4 4 8-9" stroke="#222" stroke-width="2.4" fill="none"/></svg>Customized Strength Training Program</li>
    <li><svg width="14" height="12"><path d="M1 6l4 4 8-9" stroke="#222" stroke-width="2.4" fill="none"/></svg>Each Exercise Demonstrated in HD Videos</li>
    <li><svg width="14" height="12"><path d="M1 6l4 4 8-9" stroke="#222" stroke-width="2.4" fill="none"/></svg>Personalized Cardio Program</li>
    <li><svg width="14" height="12"><path d="M1 6l4 4 8-9" stroke="#222" stroke-width="2.4" fill="none"/></svg>Personalized Nutrition Coaching &amp; Meal Plans</li>
  </ul>
  <a class="btn btn-dark">More Details</a>
</div>

<div class="plan" style="left:795px">
  <svg class="plan-corner" viewBox="0 0 330 553"><polygon points="330,120 330,553 120,553" fill="#f4ee1e" opacity=".35"/></svg>
  <h3>Elite</h3>
  <div class="price"><sup>$</sup><b>249</b><small>month</small></div>
  <ul class="features">
    <li><svg width="14" height="12"><path d="M1 6l4 4 8-9" stroke="#222" stroke-width="2.4" fill="none"/></svg>Weekly 30 Minute In-Person or Phone Consultation</li>
    <li><svg width="14" height="12"><path d="M1 6l4 4 8-9" stroke="#222" stroke-width="2.4" fill="none"/></svg>Unlimited In-App Messaging Support</li>
    <li><svg width="14" height="12"><path d="M1 6l4 4 8-9" stroke="#222" stroke-width="2.4" fill="none"/></svg>Weekly Customized Strength Training Program</li>
    <li><svg width="14" height="12"><path d="M1 6l4 4 8-9" stroke="#222" stroke-width="2.4" fill="none"/></svg>Each Exercise Demonstrated in HD Videos</li>
    <li><svg width="14" height="12"><path d="M1 6l4 4 8-9" stroke="#222" stroke-width="2.4" fill="none"/></svg>Weekly Customized Cardio Training Program</li>
    <li><svg width="14" height="12"><path d="M1 6l4 4 8-9" stroke="#222" stroke-width="2.4" fill="none"/></svg>Bi-Weekly Nutrition Coaching &amp; Meal Plans</li>
  </ul>
  <a class="btn btn-dark">More Details</a>
</div>

<section class="supplements">
  <svg class="abs" style="left:0;top:0" width="1200" height="888" viewBox="0 0 1200 888">
    <polygon points="1200,150 1200,888 420,888" fill="#2c2c2c"/>
    <polygon points="0,620 0,888 420,888" fill="#ffffff"/>
  </svg>
</section>
<div class="section-mark" style="top:2116px;border-color:var(--white)"></div>
<h2 class="section-title" style="top:2189px;color:var(--white)">Supplements</h2>
<div class="underline" style="top:2242px"></div>

<h3 class="product-name" style="left:80px;top:2322px;color:var(--white)">Vima <span>Blaze</span></h3>
<div class="prod-bar" style="left:80px;top:2382px"></div>
<p class="abs body-copy" style="left:80px;top:2408px;width:540px;color:#dddddd">Lorem ipsum dolor sit amet, consectetur adipisicing elit, sed do eiusmod tempor incididunt ut labore et doloreades magna aliqua. Ut enim ad minim veniam, quis nostrud exercitation ullamco laboris nisi ut aliquip ex ea commodo consequat. Duis aute irure dolor in reprehenderit in voluptate velit esse cillum ..</p>
<a class="btn btn-yellow" style="left:80px;top:2606px;width:180px">Read More</a>
<div class="product-image" style="left:780px;top:2343px;width:254px;height:438px;border-radius:40px 40px 22px 22px;background:linear-gradient(90deg,#111 0%,#3a3a3a 45%,#111 100%)" role="img" aria-label="Black supplement bottle with yellow label, 60 capsules"></div>

<section class="vima-rise">
  <svg class="abs" style="left:0;top:2947px" width="1200" height="644" viewBox="0 0 1200 644">
    <polygon points="1200,340 1200,644 640,644" fill="#3a3a3a"/>
  </svg>
  <div class="product-image" style="left:82px;top:3059px;width:483px;height:357px;background:linear-gradient(120deg,#e6e6e6 0%,#bdbdbd 50%,#f1b23a 85%,#e08a2a 100%)" role="img" aria-label="Supplement box in grey with yellow title and peach tea fruit"></div>
  <h3 class="product-name" style="left:617px;top:3005px;color:var(--ink)">Vima <span style="color:#d9d100">Rise</span></h3>
  <div class="prod-bar" style="left:617px;top:3065px"></div>
  <p class="abs body-copy" style="left:617px;top:3090px;width:520px;color:var(--text)">Lorem ipsum dolor sit amet, consectetur adipisicing elit, sed do eiusmod tempor incididunt ut labore et doloreades magna aliqua. Ut enim ad minim veniam, quis nostrud exercitation ullamco laboris nisi ut aliquip ex ea commodo consequat. Duis aute irure dolor in reprehenderit in voluptate velit esse cillum ..</p>
  <a class="btn btn-yellow" style="left:617px;top:3290px;width:180px">Read More</a>
</section>

<section class="about"></section>
<div class="section-mark" style="top:3652px"></div>
<h2 class="section-title" style="top:3724px">What We Do</h2>
<div class="underline" style="top:3778px"></div>
<div class="abs" style="left:79px;top:3854px;width:507px;height:336px;background:linear-gradient(110deg,#4d5a3a 0%,#8b8f6e 45%,#c9c0a8 100%)" role="img" aria-label="Photo of a trainer and a client looking at a tablet outdoors"></div>
<p class="abs body-copy" style="left:614px;top:3852px;width:520px;color:var(--muted)">Lorem ipsum dolor sit amet, consectetur adipisicing elit, sed do eiusmod tempor incididunt ut labore et doloreades magna aliqua. Ut enim ad minim veniam, quis nostrud exercitation ullamco laboris nisi ut aliquip ex ea commodo consequat. Duis aute irure dolor in reprehenderit in voluptate velit esse cillum dolore eu fugiat nulla pariatur. Excepteur sint occaecat cupidatat non proident, sunt in culpa qui officia deserunt mollit anim id est laborum.</p>
<a class="btn btn-dark" style="left:614px;top:4120px;width:180px">Read More</a>

<footer class="site-footer">
  <svg class="abs" style="left:0;top:0" width="430" height="257" viewBox="0 0 430 257">
    <polygon points="0,0 340,0 420,257 0,257" fill="#161616"/>
  </svg>
  <div class="abs" style="left:70px;top:92px;display:flex;align-items:center;gap:10px;color:var(--yellow);font-weight:700;font-size:15px;letter-spacing:1.5px;text-transform:uppercase"><span style="width:18px;height:18px;border-radius:50%;background:var(--yellow)"></span>Brinova Motion</div>
  <p class="abs" style="left:60px;top:150px;width:200px;text-align:center;color:#cccccc;font-size:12px;line-height:18px">Copyright © 2018 Company Name.<br>All Rights Reserved.</p>
</footer>
<div class="subscribe-label">Email Subscribe:</div>
<div class="subscribe-input">Email Address</div>
<div class="subscribe-btn">SIGN UP</div>
<nav class="foot-nav">
  <a style="left:583px" href="#">Home</a>
  <a style="left:662px" href="#">Programs</a>
  <a style="left:775px" href="#">About</a>
  <a style="left:862px" href="#">FAQ</a>
  <a style="left:925px" href="#">Contact</a>
  <a style="left:1030px" href="#">Supplements</a>
</nav>
<span class="social" style="left:988px"></span>
<span class="social" style="left:1023px"></span>
<span class="social" style="left:1058px"></span>
<span class="social" style="left:1093px"></span>

</body>
</html>
```